International Petrochemical business needs a web design for Tessaro Desk system

We need a web design for a "Tessaro Desk" system for an international petrochemical company. The web site is used internally within the company. It is hosted by an internal department which provides government permit request service for other departments.

We would like to see designs of two pages using color light blue. (home page, internal page as attached).
Home Page:
1. Header has a background image and small animation. Header on home page can be taller than the header of the internal page.
2. Layout as attached.

Internal Page:
1. Header can use the same background image as the home page and can be shorter to utilize the page for content.
2. The blue icon behind every captions represent an icon. When user move mouse over this icon, it displays the caption in Thai language as a tooltip. This icon needs to be redesign.

The final design should communicate the followings:
- Excellent service provided system in terms of time and accurary
- Rapid growth of business via building petrochemical refinery plant

For Internal Page, the blue circle behind every captions represent an icon. When mouse over this icon, a tool tip showing the caption in Thai language is shown. Please also design this icon..

There are more feedbacks from customer as followed:

1. Banner should consists of 
    1.1 "Approved" stamp on paper
    1.2 An image of Garuda. It is used on every government documents in Thailand
    1.3 Image of petrochemical plant
2. Each menu item (Home, Permit, Search, etc) should have different colors. Drop down menu will use the same color as its parent menu item.
3. Overall tone of the web page should be light blue with background of the body the web page in white
4. "New Request" button should use green color with icon on it
5. Table header of each box in the body of the page should use dark blue background with text in white

Please kindly submit your revisions.
Thank you.

Reason: We get some late feedbacks from customers which was just updated to all designers.

• 1. Design for 1024x768 screen resolution
2. Use light blue theme
3. Background of header where the company logo is must have white background

```html
<!DOCTYPE html>
<html lang="en">
<head>
<meta charset="utf-8">
<title>Tessaro Desk – Request Form</title>
<link rel="stylesheet" href="https://fonts.googleapis.com/css2?family=Noto+Sans:wght@400;700&family=Noto+Sans+Thai:wght@400;700&display=swap">
<style>
:root{
  --brand-blue:#0d5aa7;
  --title-blue:#163f72;
  --icon-navy:#1d3f73;
  --panel-bg:#eef6fc;
  --panel-border:#c9d3dc;
  --text:#222;
  --muted:#555;
  --input-border:#cfd5da;
  --link:#1a64c8;
  --chip-bg:#d4d6d8;
  --footer:#0d5aa7;
  --nav-home:#45b3cf;
  --nav-permits:#49b55a;
  --nav-search:#e1aa27;
  --nav-report:#c9474c;
  --nav-admin:#6aa06a;
  --nav-help:#6a3fa2;
  --required:#e02020;
}
*{box-sizing:border-box;margin:0;padding:0}
html,body{width:834px;height:1200px;overflow:hidden;background:#fff}
body{position:relative;font-family:"Noto Sans",sans-serif;color:var(--text);font-size:11px}
.top-rule{position:absolute;left:0;top:0;width:834px;height:3px;background:var(--brand-blue)}
.brand{position:absolute;left:48px;top:18px;display:flex;align-items:center;gap:7px}
.brand-mark{width:28px;height:28px;border-radius:50%;background:var(--brand-blue)}
.brand-name{font-weight:700;font-size:14px;line-height:14px;color:var(--brand-blue);width:130px}
.site-title{position:absolute;right:42px;top:24px;font-weight:700;font-size:28px;letter-spacing:1px;color:var(--title-blue)}
.main-nav{position:absolute;top:66px;left:0;width:834px;height:24px}
.main-nav a{position:absolute;top:0;height:24px;width:72px;border-radius:6px 6px 0 0;color:#fff;font-size:11px;font-weight:700;text-decoration:none;text-align:center;line-height:25px;text-transform:uppercase;text-shadow:0 1px 1px rgba(0,0,0,.35);box-shadow:inset 0 6px 8px rgba(255,255,255,.35)}
.nav-home{left:316px;background:var(--nav-home)}
.nav-permits{left:397px;background:var(--nav-permits)}
.nav-search{left:479px;background:var(--nav-search)}
.nav-report{left:560px;background:var(--nav-report)}
.nav-admin{left:641px;background:var(--nav-admin)}
.nav-help{left:723px;background:var(--nav-help)}
.banner{position:absolute;left:12px;top:90px;width:810px;height:138px;background:linear-gradient(90deg,#6f7f92 0%,#a9b9cc 35%,#5d7ea6 60%,#cfe3f4 100%)}
.panel{position:absolute;left:47px;top:249px;width:758px;height:856px;background:var(--panel-bg);border:1px solid var(--panel-border);border-radius:4px;box-shadow:0 1px 3px rgba(0,0,0,.15)}
.panel-head{height:36px;background:linear-gradient(#2d7fca,#0f5aa3);border-radius:3px 3px 0 0;color:#fff;font-weight:700;font-size:14px;line-height:36px;padding-left:11px}
.field{position:absolute;left:0;height:28px;width:420px}
.field-right{left:400px;width:340px}
.field-label{position:absolute;left:0;top:0;width:131px;text-align:right;font-weight:700;font-size:11px;line-height:28px;white-space:nowrap}
.req{color:var(--required);font-size:9px;vertical-align:top;position:relative;top:-4px}
.field-icon{position:absolute;left:137px;top:0;width:28px;height:28px}
.colon{position:absolute;left:171px;top:0;line-height:28px;font-weight:700}
.control{position:absolute;left:183px;top:4px;height:21px;width:207px;background:#fff;border:1px solid var(--input-border);border-top:2px solid #c2c6ca;border-radius:3px;font-size:11px;color:var(--muted);padding-left:8px;line-height:18px;white-space:nowrap}
.field-right .control{width:148px}
.select::after{content:"";position:absolute;right:4px;top:5px;border:6px solid transparent;border-top:8px solid #6b6b6b;border-bottom:0}
.date-day{width:36px}
.date-month{left:226px;width:73px}
.date-year{left:306px;width:45px}
.textarea{height:73px;top:0}
.tooltip{position:absolute;left:448px;top:113px;width:132px;height:38px;background:var(--icon-navy);border-radius:4px;color:#fff;font-family:"Noto Sans Thai",sans-serif;font-size:8.5px;line-height:12px;padding:5px 8px;white-space:nowrap}
.tooltip::before{content:"";position:absolute;left:98px;top:-6px;border:6px solid transparent;border-bottom-color:var(--icon-navy);border-top:0}
.btn{position:absolute;height:20px;background:linear-gradient(#f6f6f6,#d7d9da);border:1px solid #aeb2b5;border-radius:3px;font-size:10px;color:#444;text-align:center;line-height:18px}
.chips{position:absolute;left:183px;display:flex;flex-wrap:wrap;gap:4px 5px;width:250px}
.chip{background:var(--chip-bg);border:1px solid #b5b8ba;border-radius:2px;font-size:8px;font-weight:700;color:#666;height:14px;line-height:12px;padding-left:4px;display:flex;align-items:center}
.chip-x{margin-left:6px;width:18px;height:12px;background:#fff;border-left:1px solid #b5b8ba;text-align:center;font-size:8px;color:#444}
.related-table{position:absolute;left:182px;top:683px;width:320px;height:122px;background:#fff;border-radius:3px;border-collapse:collapse;font-size:10px}
.related-table thead th{background:linear-gradient(#fafafa,#cfd2d4);height:25px;font-weight:700;color:#555;text-align:left;padding-left:10px;border-right:1px solid #c7c9cb}
.related-table thead th:last-child{border-right:0}
.related-table td{padding-left:10px;height:14.5px;font-size:9.5px;line-height:14px}
.related-table td a{color:var(--link)}
.pager{position:absolute;left:310px;top:783px;display:flex}
.pager span{width:22px;height:18px;border:1px solid #d6dadd;text-align:center;line-height:16px;font-size:11px;color:var(--link);background:#fff}
.pager .current{color:#999;background:#f1f1f1}
.action{position:absolute;top:815px;height:28px;font-size:12.5px;color:#555;line-height:26px;background:linear-gradient(#fafafa,#d5d8da);border:1px solid #9fa4a8;border-radius:3px;box-shadow:0 1px 2px rgba(0,0,0,.2)}
.btn-back{left:181px;width:91px;padding-left:46px;text-align:left}
.btn-back svg{position:absolute;left:0;top:0}
.btn-create{left:280px;width:222px;text-align:center}
.footer{position:absolute;left:0;top:1125px;width:834px;height:75px;background:var(--footer);color:#fff;font-size:8px}
.footer .copy{position:absolute;left:58px;top:14px}
.footer .legal{position:absolute;right:42px;top:14px}
</style>
</head>
<body>
<div class="top-rule"></div>
<header>
  <div class="brand"><span class="brand-mark"></span><span class="brand-name">NORVANE PETROCHEMICAL</span></div>
  <div class="site-title">TESSARO DESK</div>
  <nav class="main-nav">
    <a class="nav-home" href="#">Home</a>
    <a class="nav-permits" href="#">Permits</a>
    <a class="nav-search" href="#">Search</a>
    <a class="nav-report" href="#">Report</a>
    <a class="nav-admin" href="#">Admin</a>
    <a class="nav-help" href="#">Help</a>
  </nav>
  <div class="banner" role="img" aria-label="Banner: Garuda emblem, petrochemical refinery plant and a red Approved stamp on paper"></div>
</header>

<main class="panel">
  <div class="panel-head">Request Form</div>

  <div class="field" style="top:46px">
    <span class="field-label">Request Date</span>
    <svg class="field-icon" viewBox="0 0 28 28"><rect width="28" height="28" rx="5" fill="var(--icon-navy)"/><rect x="6" y="8" width="16" height="13" fill="none" stroke="#fff" stroke-width="1.6"/><rect x="6" y="8" width="16" height="3" fill="#fff"/><rect x="12" y="13" width="4" height="5" fill="#fff"/></svg>
    <span class="colon">:</span>
    <div class="control date-day">21</div>
    <div class="control date-month select">January</div>
    <div class="control date-year">2013</div>
  </div>

  <div class="field field-right" style="top:46px">
    <span class="field-label">Requester Employee No</span>
    <svg class="field-icon" viewBox="0 0 28 28"><rect width="28" height="28" rx="5" fill="var(--icon-navy)"/><circle cx="14" cy="14" r="9" fill="none" stroke="#fff" stroke-width="1.6"/><text x="14" y="17.5" font-size="9" font-weight="700" fill="#fff" text-anchor="middle" font-family="Noto Sans,sans-serif">10</text></svg>
    <span class="colon">:</span>
    <div class="control">3071 52864 1180</div>
  </div>

  <div class="field" style="top:81px">
    <span class="field-label">Requester Name</span>
    <svg class="field-icon" viewBox="0 0 28 28"><rect width="28" height="28" rx="5" fill="var(--icon-navy)"/><rect x="5" y="8" width="18" height="12" rx="1" fill="none" stroke="#fff" stroke-width="1.6"/><circle cx="10" cy="13" r="2" fill="#fff"/><rect x="8" y="16" width="5" height="2" fill="#fff"/><rect x="15" y="12" width="6" height="1.5" fill="#fff"/><rect x="15" y="15" width="6" height="1.5" fill="#fff"/></svg>
    <span class="colon">:</span>
    <div class="control">Peter Halden</div>
  </div>

  <div class="field field-right" style="top:81px">
    <span class="field-label">Telephone</span>
    <svg class="field-icon" viewBox="0 0 28 28"><rect width="28" height="28" rx="5" fill="var(--icon-navy)"/><path d="M9 7l3 0 1 4-2 1.5c1 2 2.5 3.5 4.5 4.5l1.5-2 4 1 0 3c-6 1-13-6-12-12z" fill="#fff"/></svg>
    <span class="colon">:</span>
    <div class="control">2730 8152 964</div>
  </div>

  <div class="tooltip">ระหว่างดำเนินการรอดำเนินก<br>ารรอดำเนินการ</div>

  <div class="field" style="top:117px">
    <span class="field-label">Contact No</span>
    <svg class="field-icon" viewBox="0 0 28 28"><rect width="28" height="28" rx="5" fill="var(--icon-navy)"/><rect x="9" y="5" width="10" height="18" rx="2" fill="none" stroke="#fff" stroke-width="1.6"/><rect x="11" y="8" width="6" height="6" fill="#fff"/><circle cx="14" cy="19" r="1.3" fill="#fff"/></svg>
    <span class="colon">:</span>
    <div class="control">0845 2291 7306</div>
  </div>

  <div class="field" style="top:152px">
    <span class="field-label">Company <span class="req">*</span></span>
    <svg class="field-icon" viewBox="0 0 28 28"><rect width="28" height="28" rx="5" fill="var(--icon-navy)"/><rect x="6" y="8" width="16" height="13" fill="none" stroke="#fff" stroke-width="1.6"/><path d="M10 11v7M14 11v7M18 11v7" stroke="#fff" stroke-width="2"/></svg>
    <span class="colon">:</span>
    <div class="control select">Please select</div>
  </div>

  <div class="field" style="top:188px">
    <span class="field-label">Branch <span class="req">*</span></span>
    <svg class="field-icon" viewBox="0 0 28 28"><rect width="28" height="28" rx="5" fill="var(--icon-navy)"/><rect x="11" y="5" width="6" height="5" fill="#fff"/><path d="M14 10v4M8 14h12M8 14v3M20 14v3" stroke="#fff" stroke-width="1.5" fill="none"/><rect x="5" y="17" width="6" height="5" fill="#fff"/><rect x="17" y="17" width="6" height="5" fill="#fff"/></svg>
    <span class="colon">:</span>
    <div class="control select">Please select</div>
  </div>

  <div class="field" style="top:223px">
    <span class="field-label">Document Category <span class="req">*</span></span>
    <svg class="field-icon" viewBox="0 0 28 28"><rect width="28" height="28" rx="5" fill="var(--icon-navy)"/><path d="M8 5h10l3 3v15H8z" fill="none" stroke="#fff" stroke-width="1.5"/><path d="M10 15l3 3 6-7" fill="none" stroke="#fff" stroke-width="2"/></svg>
    <span class="colon">:</span>
    <div class="control select">Please select</div>
  </div>

  <div class="field" style="top:259px">
    <span class="field-label">Document Type <span class="req">*</span></span>
    <svg class="field-icon" viewBox="0 0 28 28"><rect width="28" height="28" rx="5" fill="var(--icon-navy)"/><path d="M8 5h9l4 4v14H8z" fill="none" stroke="#fff" stroke-width="1.5"/><text x="14.5" y="20" font-size="6" fill="#fff" text-anchor="middle" font-family="Noto Sans,sans-serif">doc</text></svg>
    <span class="colon">:</span>
    <div class="control select">Please select</div>
  </div>

  <div class="field" style="top:294px">
    <span class="field-label">Expected Use Date <span class="req">*</span></span>
    <svg class="field-icon" viewBox="0 0 28 28"><rect width="28" height="28" rx="5" fill="var(--icon-navy)"/><rect x="6" y="7" width="16" height="15" fill="none" stroke="#fff" stroke-width="1.6"/><rect x="6" y="7" width="16" height="3" fill="#fff"/><path d="M13 13h2v7" stroke="#fff" stroke-width="2" fill="none"/></svg>
    <span class="colon">:</span>
    <div class="control date-day">28</div>
    <div class="control date-month select">January</div>
    <div class="control date-year">2013</div>
  </div>

  <div class="field" style="top:330px;height:74px">
    <span class="field-label">Detail <span class="req">*</span></span>
    <svg class="field-icon" viewBox="0 0 28 28"><rect width="28" height="28" rx="5" fill="var(--icon-navy)"/><rect x="6" y="6" width="14" height="16" fill="none" stroke="#fff" stroke-width="1.5"/><path d="M9 10h8M9 13h8" stroke="#fff" stroke-width="1.4"/><path d="M14 21l8-8 2 2-8 8-3 1z" fill="#fff"/></svg>
    <span class="colon">:</span>
    <div class="control textarea">Lorem ipsum dolor sit amet</div>
  </div>

  <div class="field" style="top:418px">
    <span class="field-label">Attachment</span>
    <svg class="field-icon" viewBox="0 0 28 28"><rect width="28" height="28" rx="5" fill="var(--icon-navy)"/><path d="M17 9l-7 7a2 2 0 0 0 3 3l7-7a3.5 3.5 0 0 0-5-5l-7 7a5 5 0 0 0 7 7l5-5" fill="none" stroke="#fff" stroke-width="1.6"/></svg>
    <span class="colon">:</span>
    <div class="control">confidential.doc</div>
    <div class="btn" style="left:396px;top:3px;width:60px">BROWSE</div>
    <div class="btn" style="left:462px;top:3px;width:59px">ATTACH</div>
  </div>
  <div class="chips" style="top:446px">
    <span class="chip">file1.doc<span class="chip-x">X</span></span>
    <span class="chip">file1.doc<span class="chip-x">X</span></span>
    <span class="chip">file1.doc<span class="chip-x">X</span></span>
  </div>

  <div class="field" style="top:471px">
    <span class="field-label">Coordinator <span class="req">*</span></span>
    <svg class="field-icon" viewBox="0 0 28 28"><rect width="28" height="28" rx="5" fill="var(--icon-navy)"/><circle cx="14" cy="10" r="4" fill="#fff"/><path d="M6 23c0-5 3.5-7 8-7s8 2 8 7z" fill="#fff"/></svg>
    <span class="colon">:</span>
    <div class="btn" style="left:184px;top:4px;width:58px">ADD</div>
  </div>
  <div class="chips" style="top:499px">
    <span class="chip">Peter Halden HR<span class="chip-x">X</span></span>
  </div>

  <div class="field" style="top:524px">
    <span class="field-label">Related Person <span class="req">*</span></span>
    <svg class="field-icon" viewBox="0 0 28 28"><rect width="28" height="28" rx="5" fill="var(--icon-navy)"/><circle cx="10" cy="11" r="3.5" fill="#fff"/><circle cx="18" cy="11" r="3.5" fill="#fff"/><path d="M3 21c0-4 3-6 7-6s7 2 7 6zM13 21c0-4 1-6 5-6s7 2 7 6z" fill="#fff"/></svg>
    <span class="colon">:</span>
    <div class="btn" style="left:184px;top:4px;width:58px">ADD</div>
  </div>
  <div class="chips" style="top:552px;width:220px">
    <span class="chip">Clara Moss (IT)<span class="chip-x">X</span></span>
    <span class="chip">Owen Larkin (Finance)<span class="chip-x">X</span></span>
    <span class="chip">Ray Dorsett (Finance)<span class="chip-x">X</span></span>
  </div>

  <div class="field" style="top:596px;height:74px">
    <span class="field-label">Remark</span>
    <svg class="field-icon" viewBox="0 0 28 28"><rect width="28" height="28" rx="5" fill="var(--icon-navy)"/><rect x="5" y="8" width="18" height="12" rx="2" fill="none" stroke="#fff" stroke-width="1.6"/><circle cx="10" cy="14" r="1.3" fill="#fff"/><circle cx="14" cy="14" r="1.3" fill="#fff"/><circle cx="18" cy="14" r="1.3" fill="#fff"/></svg>
    <span class="colon">:</span>
    <div class="control textarea" style="height:71px">Lorem ipsum dolor sit amet</div>
  </div>

  <div class="field" style="top:684px">
    <span class="field-label">Related Request</span>
    <svg class="field-icon" viewBox="0 0 28 28"><rect width="28" height="28" rx="5" fill="var(--icon-navy)"/><ellipse cx="15" cy="12" rx="8" ry="6" fill="#fff"/><path d="M9 16l-3 5 6-3z" fill="#fff"/><ellipse cx="10" cy="15" rx="4" ry="3" fill="none" stroke="var(--icon-navy)" stroke-width="1"/></svg>
    <span class="colon">:</span>
  </div>

  <table class="related-table">
    <thead>
      <tr><th>Request No.</th><th>Request Date</th><th>Company</th><th>Branch</th></tr>
    </thead>
    <tbody>
      <tr><td style="padding-top:6px"><a href="#">AB56001</a></td><td style="padding-top:6px">20/4/2013</td><td style="padding-top:6px">NVP</td><td style="padding-top:6px">GC1</td></tr>
      <tr><td><a href="#">BIO5502</a></td><td>21/4/2013</td><td>NVP</td><td>GC2</td></tr>
      <tr><td><a href="#">AB56001</a></td><td>20/4/2013</td><td>ZRQ</td><td>GC3</td></tr>
      <tr><td><a href="#">BIO5502</a></td><td>21/4/2013</td><td>ZRQ</td><td>GC4</td></tr>
      <tr><td colspan="4" style="height:34px"></td></tr>
    </tbody>
  </table>
  <div class="pager"><span class="current">1</span><span>2</span><span>3</span><span>4</span></div>

  <div class="action btn-back">
    <svg width="37" height="26" viewBox="0 0 37 26"><rect x="0" y="0" width="37" height="26" rx="2" fill="#e9ebec"/><path d="M36.5 0v26" stroke="#aeb2b5"/><path d="M21 7l-6 6 6 6" fill="none" stroke="#333" stroke-width="2.4"/></svg>
    BACK
  </div>
  <div class="action btn-create">CREATE NEW REQUEST</div>
</main>

<footer class="footer">
  <span class="copy">Copyright © 2013 NorvanePetrochemical. All rights reserved.</span>
  <span class="legal">Terms and Condition | Privacy</span>
</footer>
</body>
</html>
```